Velmora Fresh Greens Square Trifold Brochure

We need a powerful informational square tri-fold brochure for a new product that is set to change the health of us all. Known as Spirulina, a blue green algae superfood, consumed by people for thousands of years. The reason why life exists on this planet. Sold commercially in stores worldwide as a supplement in dead powder form, until now! We have perfected systems to capture the delicate cells, pack and ship to customers fresh. This whole food gourmet supreme is a game changer for us all.
We need an educational informational card that dramatically captures the attention of everyone. Giving them enough information to bring their curiosity and intrigue to the website to learn more but also having good knowledge base to hold in their hand for those that don't use a computer.
The front of the card should grab their attention (possibly with image of the jar with water below) with the rest for more detailed information, making it clear that this is delicious, raw, living, fresh, pure, super nutrition grown in USA, safe, laboratory tested, etc.
Design should match font, color and design of the website. Very clear, professional, eye catching and very powerful and dramatic. Looking for the best ever!
The ultimate living enzymatically active bioavailable raw plant based nutrients. Grown in spring water using the highest quality natural and organic food grade nutrients, in enclosed greenhouses in Florida.
When we say fresh, we really mean it!
The only truly living Spirulina.
You have to try it at least once.

**May add a bit of sex appeal if done with class. www.velmorafreshgreens.example

Thank you so much, extra special reward for the designer who grabs our attention the best!
Please contact us if you need additional images from the website for your design. Design Ideas we like that grabbed our attention attached below. Just ideas.

Target Market(s)

Health conscious, vegan, bodybuilding, sexy, fitness,

Industry/Entity Type

Health And Wellness

Font styles to use
Serif
Sans Serif

Colors

Designer to choose colors to be used in the design.

Requirements
Must have
• Square design, Powerful info - graphic(s), Color theme to match website and brand. Dynamic message knowledge based theme. Love simple design easy to read. Sections:
• Front cover: Product Jar with water (image) dramatic
• (Sections from Website) Health Benefits, Nutritional Profile, Lab Tested, How its Grown, What is Velmora Fresh Greens,
• Bold Plant based Images to highlight plant based Nutrition
• Include Section with Institutional Quotes KELT, BRMQ, GLX, etc.
Nice to have
• Love to see very creative outside the box design. A Wow head turner! Sexy but simple, classy and elegant.
Should not have
• Please no clutter.

```html
<!DOCTYPE html>
<html lang="en">
<head>
<meta charset="utf-8">
<title>Velmora Fresh Greens — Square Trifold, Inside Spread</title>
<link href="https://fonts.googleapis.com/css2?family=Montserrat:wght@300;400;600&family=Open+Sans:wght@400;700&display=swap" rel="stylesheet">
<style>
  :root {
    --stage: #c7ccd1;
    --forest: #132217;
    --forest-deep: #0e1a11;
    --forest-glass: rgba(16, 38, 22, 0.86);
    --ink-light: #e9efe9;
    --ink-dark: #111111;
    --paper: #ffffff;
    --rule: #d9e3da;
  }
  * { box-sizing: border-box; margin: 0; padding: 0; }
  html, body {
    width: 1200px; height: 800px; overflow: hidden;
    background: var(--stage);
    font-family: "Montserrat", sans-serif;
  }
  .spread {
    position: absolute; left: 30px; top: 210px;
    width: 1140px; height: 380px;
    display: flex;
    box-shadow: 0 10px 30px rgba(0,0,0,0.25);
  }
  .panel { position: relative; width: 380px; height: 380px; overflow: hidden; }

  /* Panel 1 — health benefits */
  .panel--benefits { background: var(--forest); }
  .panel__photo {
    position: absolute; inset: 0;
  }
  .panel--benefits .panel__photo {
    background: radial-gradient(ellipse at 45% 65%, #3a4a3b 0%, #223326 40%, var(--forest) 80%);
  }
  .panel__title {
    position: relative;
    text-align: center;
    color: var(--ink-light);
    font-weight: 400; font-size: 17px; letter-spacing: 1px;
    padding-top: 22px;
  }
  .panel__title::after {
    content: ""; display: block; width: 110px; height: 1px;
    background: var(--rule); margin: 7px auto 0;
  }
  .benefit-grid {
    position: relative;
    display: grid; grid-template-columns: 1fr 1fr;
    column-gap: 14px; padding: 16px 18px 0;
  }
  .benefit-list, .nutrient-list { list-style: none; }
  .benefit-list li, .nutrient-list li {
    display: flex; align-items: center; gap: 9px;
    color: var(--ink-light);
    font-size: 8.5px; line-height: 1.15; text-transform: uppercase;
  }
  .benefit-list li { height: 41px; }
  .icon-disc {
    flex: none; width: 34px; height: 34px; border-radius: 50%;
    border: 2px solid #f2f2f2;
  }

  /* Panel 2 — nutritional profile */
  .panel--profile { background: var(--forest-deep); }
  .nutrient-grid {
    display: grid; grid-template-columns: 1fr 1fr;
    column-gap: 14px; padding: 14px 20px 0;
  }
  .nutrient-list li { height: 35px; }
  .nutrient-list .icon-disc { width: 30px; height: 30px; }
  .tagline {
    position: absolute; left: 0; right: 0; bottom: 0; height: 82px;
    background: var(--paper);
    display: flex; flex-direction: column; justify-content: center; align-items: center;
    font-family: "Open Sans", sans-serif; font-weight: 700;
    font-size: 12.5px; color: var(--ink-dark); line-height: 1.4;
  }

  /* Panel 3 — story boxes over lab scene */
  .panel--story .panel__photo {
    background: linear-gradient(180deg, #8f93ab 0%, #c9ccd8 45%, #b9c0c4 68%, #2f6a35 82%, #1f4d25 100%);
  }
  .story-grid {
    position: relative;
    display: grid; grid-template-columns: 1fr 1fr; grid-template-rows: 1fr 1fr;
    gap: 10px; padding: 14px; height: 100%;
  }
  .story-card {
    background: var(--forest-glass);
    border-radius: 12px;
    padding: 12px 11px;
    color: var(--ink-light);
    font-family: "Open Sans", sans-serif;
  }
  .story-card__title {
    font-family: "Montserrat", sans-serif; font-weight: 400;
    text-align: center; font-size: 10px; text-transform: uppercase;
    line-height: 1.25; margin-bottom: 8px;
  }
  .story-card p { font-size: 7.2px; line-height: 1.45; text-align: justify; margin-bottom: 5px; }
</style>
</head>
<body>
<main class="spread">

  <section class="panel panel--benefits">
    <div class="panel__photo" role="img" aria-label="Photo of a fit woman in a push-up pose on a dark green toned background"></div>
    <h2 class="panel__title">HEALTH BENEFITS</h2>
    <div class="benefit-grid">
      <ul class="benefit-list">
        <li><span class="icon-disc" role="img" aria-label="Cell photo" style="background:#3f8fb3"></span>Fighting cancer with living nutrition</li>
        <li><span class="icon-disc" role="img" aria-label="Waist measuring photo" style="background:#c9a48f"></span>Natural weight reducing agent</li>
        <li><span class="icon-disc" role="img" aria-label="Workout photo" style="background:#6b6b70"></span>Increasing muscle strength and endurance</li>
        <li><span class="icon-disc" role="img" aria-label="Blood cells photo" style="background:#c7607a"></span>Treating anemia</li>
        <li><span class="icon-disc" role="img" aria-label="Brain vessels photo" style="background:#c58a2c"></span>Lowering risk of stroke</li>
        <li><span class="icon-disc" role="img" aria-label="Skin care photo" style="background:#e0c3ad"></span>Slows aging</li>
        <li><span class="icon-disc" role="img" aria-label="Joint pain photo" style="background:#d9aaa6"></span>Arthritis anti-inflammatory</li>
      </ul>
      <ul class="benefit-list">
        <li><span class="icon-disc" role="img" aria-label="Artery photo" style="background:#c5566a"></span>Cholesterol buster</li>
        <li><span class="icon-disc" role="img" aria-label="Glucose test photo" style="background:#d8b1a5"></span>Managing blood sugar</li>
        <li><span class="icon-disc" role="img" aria-label="Allergy photo" style="background:#e3d5c8"></span>Treating allergies</li>
        <li><span class="icon-disc" role="img" aria-label="Liver scan photo" style="background:#2f8db0"></span>Protecting your liver</li>
        <li><span class="icon-disc" role="img" aria-label="Eye photo" style="background:#8ea0ab"></span>Preventing blindness</li>
        <li><span class="icon-disc" role="img" aria-label="Wellness photo" style="background:#e6ddd6"></span>Wide spectrum anti-toxic</li>
        <li><span class="icon-disc" role="img" aria-label="Skin beauty photo" style="background:#e9d3c2"></span>Dermatology and beyond skin beauty</li>
      </ul>
    </div>
  </section>

  <section class="panel panel--profile">
    <h2 class="panel__title">NUTRITIONAL PROFILE</h2>
    <div class="nutrient-grid">
      <ul class="nutrient-list">
        <li><span class="icon-disc" role="img" aria-label="Green algae texture" style="background:#6fbf4a"></span>Chlorophyl powering energy from light</li>
        <li><span class="icon-disc" role="img" aria-label="Vitamin molecules" style="background:#6c9ad0"></span>Bioavailable living vitamins</li>
        <li><span class="icon-disc" role="img" aria-label="Antioxidant molecule" style="background:#efe6f2"></span>Antioxidants</li>
        <li><span class="icon-disc" role="img" aria-label="Amino acid structure" style="background:#3a4e77"></span>Amino acids</li>
        <li><span class="icon-disc" role="img" aria-label="Enzyme structure" style="background:#b8d2df"></span>Superoxide dismutase</li>
        <li><span class="icon-disc" role="img" aria-label="Fatty acid molecule" style="background:#f1eef0"></span>Omega 6 fatty acids</li>
      </ul>
      <ul class="nutrient-list">
        <li><span class="icon-disc" role="img" aria-label="Blue pigment vial" style="background:#5e8fa8"></span>Phycocyanin super pigment</li>
        <li><span class="icon-disc" role="img" aria-label="Mineral crystals" style="background:#3f9a74"></span>Minerals for cellular communication</li>
        <li><span class="icon-disc" role="img" aria-label="Plant cells" style="background:#8f63a3"></span>Fighter phytonutrients</li>
        <li><span class="icon-disc" role="img" aria-label="Protein cell" style="background:#5fa0b8"></span>Complete protein</li>
        <li><span class="icon-disc" role="img" aria-label="Omega molecule" style="background:#f3efe6"></span>Omega 3 fatty acids</li>
        <li><span class="icon-disc" role="img" aria-label="Enzyme cluster" style="background:#4d74a8"></span>Enzymes</li>
      </ul>
    </div>
    <div class="tagline">
      <span>Experience something completely different.</span>
      <span>The most powerful superfood in the world.</span>
    </div>
  </section>

  <section class="panel panel--story">
    <div class="panel__photo" role="img" aria-label="Laboratory scene with a product jar and green culture vessels"></div>
    <div class="story-grid">
      <article class="story-card">
        <h3 class="story-card__title">Microbiologist<br>Dorian Kell</h3>
        <p>We were impressed with the unique methods of cultivation and harvesting developed by this team. The fresh culture keeps its living cells intact and its nutrients fully active.</p>
        <p>Amazing, isn't it? There's even more...</p>
      </article>
      <article class="story-card">
        <h3 class="story-card__title">Arthrospira<br>Maxima X1</h3>
        <p>Our culture was isolated from a pristine alkaline lake and kept in a certified collection.</p>
        <p>We received the original strain and have been growing this culture since 2014.</p>
      </article>
      <article class="story-card">
        <h3 class="story-card__title">Farming</h3>
        <p>Velmora Fresh Greens is a unique strain of algae grown in spring water inside enclosed greenhouses in Florida. Each batch is tested to meet strict standards for purity and safety.</p>
        <p>The Future of Nutrition<br>– BRMQ</p>
      </article>
      <article class="story-card">
        <h3 class="story-card__title">Harvesting</h3>
        <p>Velmora Fresh Greens is a fragile organism that needs gentle care. We harvest by hand, rinse in cool spring water and pack the living paste within hours for delivery.</p>
      </article>
    </div>
  </section>

</main>
</body>
</html>
```